Word Studio Lindqvara Templates

We run a large number of businesses, including schools, airports, hotels and offices. We write reports on a daily basis and are looking for a strong and sexy WORD Template. We already have a logo in place (see graphical chart attached), that is rights' protected. We are looking for a beautiful wich reflect modern design and human aspects. Our logo has 2 design, full fill and watermark. It can be used in red or black.

Target Market(s)

Architects, Fire brigade, Building investors, contactors

Font styles to use
Other font styles liked:
• Arial, Calibri, ...

Requirements
Must have
• Cover page, summary, Bullet points, Tables, Figures, Annex

```html
<!DOCTYPE html>
<html lang="en">
<head>
<meta charset="utf-8">
<title>Studio Lindqvara – Report Template Pages</title>
<link rel="stylesheet" href="https://fonts.googleapis.com/css2?family=Carlito:wght@400;700&display=swap">
<style>
:root{
  --backdrop:#a4d9dd;
  --paper:#ffffff;
  --ink:#2f2f30;
  --charcoal:#333335;
  --red:#e8382f;
  --red-deep:#c92a2a;
  --red-soft:#f0584e;
  --grey-text:#3a3a3a;
  --mist-a:#f4f4f4;
  --mist-b:#d6d6d6;
  --photo-a:#6f6b63;
  --photo-b:#b9b1a1;
  --sky-a:#4f7fb8;
  --sky-b:#c7d8ea;
}
*{box-sizing:border-box;margin:0;padding:0}
html,body{width:1200px;height:1200px;overflow:hidden}
body{background:var(--backdrop);font-family:"Carlito",Calibri,Arial,sans-serif;color:var(--ink);position:relative}
.page{position:absolute;width:245px;height:345px;box-shadow:0 2px 6px rgba(0,0,0,.12);overflow:hidden;background:var(--paper)}
.sheet{position:absolute;left:0;top:0;width:350px;height:493px;transform:scale(.7);transform-origin:0 0}
.sheet svg.art{position:absolute;left:0;top:0;width:350px;height:493px}
.p1{left:35px;top:237px}.p2{left:330px;top:237px}.p3{left:625px;top:237px}.p4{left:920px;top:237px}
.p5{left:35px;top:617px}.p6{left:330px;top:617px}

.brand-cover{position:absolute;left:28px;top:34px;display:flex;align-items:center;gap:10px}
.brand-dot{width:30px;height:30px;border-radius:50%;background:var(--red);flex:none}
.brand-cover .brand-name{color:#fff;font-size:25px;line-height:26px;font-weight:400}

.brand-header{position:absolute;right:22px;top:17px;font-size:7px;line-height:7.5px;color:var(--ink);display:flex;align-items:center;gap:3px}
.brand-header .brand-dot{width:7px;height:7px}

.page-no{position:absolute;right:30px;top:469px;font-size:5px;color:#fff}

.summary-frame{position:absolute;left:28px;top:55px;width:292px;height:280px;border:1px solid var(--red)}
.summary-title{position:absolute;left:0;right:0;top:14px;text-align:center;color:var(--red);font-weight:700;font-size:14px;text-decoration:underline;text-underline-offset:2px}
.summary-body{position:absolute;left:10px;right:10px;top:48px;font-size:5.4px;line-height:9.6px;text-align:justify;color:var(--grey-text)}
.summary-body p{margin-bottom:7px}

.contents-title{position:absolute;left:21px;top:64px;color:var(--red-deep);font-weight:700;font-size:10px}
.toc{position:absolute;left:21px;width:308px;top:84px}
.toc-row{display:flex;align-items:baseline;color:var(--ink)}
.toc-row .leader{flex:1;border-bottom:1px dotted #666;margin:0 1px;transform:translateY(-2px)}
.toc-main{font-size:9px;margin-bottom:8px}
.toc-sub{font-size:4.8px;margin-bottom:11px}
.toc-sub .num{width:24px}
.toc-main .num{width:12px}

.h1{position:absolute;left:21px;top:51px;color:var(--red-deep);font-weight:700;font-size:9px}
.body-text{position:absolute;left:40px;width:290px;font-size:5px;line-height:8.8px;text-align:justify;color:var(--grey-text)}
.body-text p{margin-bottom:6px}
.h2{position:absolute;left:21px;top:159px;color:var(--red-deep);font-weight:700;font-size:8px}
.bullets{position:absolute;left:50px;top:175px;list-style:none;font-size:5px;color:var(--grey-text)}
.bullets li{display:flex;align-items:center;gap:5px;height:11.8px}
.bullets svg{width:5px;height:5px}
.h3{position:absolute;left:21px;top:257px;color:var(--red-deep);font-weight:700;font-size:6px}
.h4{position:absolute;left:21px;top:276px;color:var(--ink);font-weight:700;font-size:6px}

.image-title{position:absolute;left:21px;top:51px;color:var(--red-deep);font-weight:700;font-size:8px}

.brand-back{position:absolute;left:0;right:0;top:440px;display:flex;justify-content:center;align-items:center;gap:6px;font-size:15px;color:var(--ink)}
.brand-back .brand-dot{width:10px;height:10px}
</style>
</head>
<body>

<!-- Cover -->
<section class="page p1" aria-label="Cover page">
  <div class="sheet">
    <svg class="art" viewBox="0 0 350 493" aria-hidden="false">
      <polygon points="0,0 350,0 350,430 0,262" fill="var(--charcoal)"/>
      <defs>
        <linearGradient id="cityCover" x1="0" y1="0" x2="1" y2="1">
          <stop offset="0" stop-color="var(--photo-a)"/>
          <stop offset="1" stop-color="var(--photo-b)"/>
        </linearGradient>
      </defs>
      <polygon role="img" aria-label="Photo of glass office towers" points="0,120 350,218 350,408 0,240" fill="url(#cityCover)"/>
      <polygon points="60,130 350,212 350,222 60,136" fill="var(--red)"/>
      <polygon points="215,58 290,36 350,120 350,205 275,148" fill="var(--red)"/>
      <polygon points="285,36 350,120 325,60" fill="var(--red-deep)"/>
      <polygon points="0,258 55,232 125,250 205,298 195,322 150,360 95,360 55,300 0,312" fill="var(--red)"/>
      <polygon points="55,232 125,250 95,300 55,300" fill="var(--red-soft)"/>
      <polygon points="95,360 150,360 140,325" fill="var(--red-deep)"/>
      <polygon points="205,298 350,405 350,430 195,322" fill="var(--charcoal)"/>
    </svg>
    <div class="brand-cover"><span class="brand-dot"></span><span class="brand-name">Studio<br>Lindqvara</span></div>
  </div>
</section>

<!-- Summary -->
<section class="page p2" aria-label="Summary page">
  <div class="sheet">
    <svg class="art" viewBox="0 0 350 493">
      <defs>
        <linearGradient id="mist" x1="0" y1="0" x2="1" y2="1">
          <stop offset="0" stop-color="var(--mist-b)"/>
          <stop offset=".45" stop-color="var(--mist-a)"/>
          <stop offset="1" stop-color="var(--mist-b)"/>
        </linearGradient>
      </defs>
      <rect role="img" aria-label="Soft grey flowing background" width="350" height="493" fill="url(#mist)"/>
    </svg>
    <div class="summary-frame">
      <h2 class="summary-title">SUMMARY</h2>
      <div class="summary-body">
        <p>Lorem ipsum dolor sit amet, consectetuer adipiscing elit, sed diam nonummy nibh euismod tincidunt ut laoreet dolore magna aliquam erat volutpat. Ut wisi enim ad minim veniam, quis nostrud exerci tation ullamcorper suscipit lobortis nisl ut aliquip ex ea commodo consequat. Duis autem vel eum iriure dolor in hendrerit in vulputate velit esse molestie consequat, vel illum dolore eu feugiat nulla facilisis at vero eros et accumsan et iusto odio dignissim qui blandit praesent luptatum zzril delenit augue duis dolore te feugait nulla facilisi.</p>
        <p>Lorem ipsum dolor sit amet, consectetuer adipiscing elit, sed diam nonummy nibh euismod tincidunt ut laoreet dolore magna aliquam erat volutpat. Ut wisi enim ad minim veniam, quis nostrud exerci tation ullamcorper suscipit lobortis nisl ut aliquip ex ea commodo consequat. Duis autem vel eum iriure dolor in hendrerit in vulputate velit esse molestie consequat, vel illum dolore eu feugiat nulla facilisis at vero eros et accumsan et iusto odio dignissim qui blandit praesent luptatum zzril delenit augue duis dolore te feugait nulla facilisi.</p>
        <p>Lorem ipsum dolor sit amet, consectetuer adipiscing elit, sed diam nonummy nibh euismod tincidunt ut laoreet dolore magna aliquam erat volutpat. Ut wisi enim ad minim veniam, quis nostrud exerci tation ullamcorper suscipit lobortis nisl ut aliquip ex ea commodo consequat. Duis autem vel eum iriure dolor in hendrerit in vulputate velit esse molestie consequat, vel illum dolore eu feugiat nulla facilisis at vero eros et accumsan et iusto odio dignissim qui blandit praesent luptatum zzril delenit augue duis dolore te feugait nulla facilisi.</p>
      </div>
    </div>
  </div>
</section>

<!-- Contents -->
<section class="page p3" aria-label="Contents page">
  <div class="sheet">
    <svg class="art" viewBox="0 0 350 493">
      <polygon points="26,14 56,14 48,23 18,23" fill="var(--charcoal)"/>
      <polygon points="36,21 272,21 266,30 28,30" fill="var(--red)"/>
      <polygon points="28,467 318,467 312,475 20,475" fill="var(--charcoal)"/>
      <polygon points="280,467 330,467 324,475 274,475" fill="var(--red)"/>
    </svg>
    <div class="brand-header"><span class="brand-dot"></span><span>Studio<br>Lindqvara</span></div>
    <h2 class="contents-title">CONTENTS</h2>
    <div class="toc">
      <div class="toc-row toc-main"><span class="num">1.</span><span>HEADING 01</span><span class="leader"></span><span>4</span></div>
      <div class="toc-row toc-sub"><span class="num">1.1.</span><span>HEADING 02</span><span class="leader"></span><span>4</span></div>
      <div class="toc-row toc-sub"><span class="num">1.1.1.</span><span>HEADING 03</span><span class="leader"></span><span>4</span></div>
      <div class="toc-row toc-sub"><span class="num">1.1.1.1.</span><span>HEADING 04</span><span class="leader"></span><span>4</span></div>
      <div class="toc-row toc-main"><span class="num">2.</span><span>IMAGE</span><span class="leader"></span><span>5</span></div>
    </div>
    <span class="page-no">Page | 3</span>
  </div>
</section>

<!-- Heading page -->
<section class="page p4" aria-label="Heading styles page">
  <div class="sheet">
    <svg class="art" viewBox="0 0 350 493">
      <polygon points="26,14 56,14 48,23 18,23" fill="var(--charcoal)"/>
      <polygon points="36,21 272,21 266,30 28,30" fill="var(--red)"/>
      <polygon points="28,467 318,467 312,475 20,475" fill="var(--charcoal)"/>
      <polygon points="280,467 330,467 324,475 274,475" fill="var(--red)"/>
    </svg>
    <div class="brand-header"><span class="brand-dot"></span><span>Studio<br>Lindqvara</span></div>
    <h2 class="h1">1.&nbsp;&nbsp; HEADING 01</h2>
    <div class="body-text" style="top:66px">
      <p>Lorem ipsum dolor sit amet, consectetuer adipiscing elit, sed diam nonummy nibh euismod tincidunt ut laoreet dolore magna aliquam erat volutpat. Ut wisi enim ad minim veniam, quis nostrud exerci tation ullamcorper suscipit lobortis nisl ut aliquip ex ea commodo consequat. Duis autem vel eum iriure dolor in hendrerit in vulputate velit esse molestie consequat, vel illum dolore eu feugiat nulla facilisis at vero eros et accumsan et iusto odio dignissim qui blandit praesent luptatum zzril delenit augue duis dolore te feugait nulla facilisi.</p>
      <p>Lorem ipsum dolor sit amet, cons ectetuer adipiscing elit, sed diam nonummy nibh euismod tincidunt ut laoreet dolore magna aliquam erat volutpat. Ut wisi enim ad minim veniam, quis nostrud exerci tation ullamcorper suscipit lobortis nisl ut aliquip ex ea commodo consequat.</p>
    </div>
    <h3 class="h2">1.1.&nbsp;&nbsp; HEADING 02</h3>
    <ul class="bullets">
      <li><svg viewBox="0 0 10 10"><circle cx="5" cy="5" r="4" fill="none" stroke="var(--red)" stroke-width="1.2"/><path d="M3 5.2l1.4 1.4L7 4" fill="none" stroke="var(--red)" stroke-width="1.2"/></svg>Lorem ipsum dolor</li>
      <li><svg viewBox="0 0 10 10"><circle cx="5" cy="5" r="4" fill="none" stroke="var(--red)" stroke-width="1.2"/><path d="M3 5.2l1.4 1.4L7 4" fill="none" stroke="var(--red)" stroke-width="1.2"/></svg>Lorem ipsum dolor</li>
      <li><svg viewBox="0 0 10 10"><circle cx="5" cy="5" r="4" fill="none" stroke="var(--red)" stroke-width="1.2"/><path d="M3 5.2l1.4 1.4L7 4" fill="none" stroke="var(--red)" stroke-width="1.2"/></svg>Lorem ipsum dolor</li>
      <li><svg viewBox="0 0 10 10"><circle cx="5" cy="5" r="4" fill="none" stroke="var(--red)" stroke-width="1.2"/><path d="M3 5.2l1.4 1.4L7 4" fill="none" stroke="var(--red)" stroke-width="1.2"/></svg>Lorem ipsum dolor</li>
      <li><svg viewBox="0 0 10 10"><circle cx="5" cy="5" r="4" fill="none" stroke="var(--red)" stroke-width="1.2"/><path d="M3 5.2l1.4 1.4L7 4" fill="none" stroke="var(--red)" stroke-width="1.2"/></svg>Lorem ipsum dolor</li>
      <li><svg viewBox="0 0 10 10"><circle cx="5" cy="5" r="4" fill="none" stroke="var(--red)" stroke-width="1.2"/><path d="M3 5.2l1.4 1.4L7 4" fill="none" stroke="var(--red)" stroke-width="1.2"/></svg>Lorem ipsum dolor</li>
    </ul>
    <h4 class="h3">1.1.1.&nbsp; HEADING 03</h4>
    <h5 class="h4">1.1.1.1.&nbsp; HEADING 04</h5>
    <span class="page-no">Page | 4</span>
  </div>
</section>

<!-- Image page -->
<section class="page p5" aria-label="Image page">
  <div class="sheet">
    <svg class="art" viewBox="0 0 350 493">
      <defs>
        <linearGradient id="meeting" x1="0" y1="0" x2="0" y2="1">
          <stop offset="0" stop-color="var(--sky-b)"/>
          <stop offset=".6" stop-color="var(--sky-a)"/>
          <stop offset="1" stop-color="#26313f"/>
        </linearGradient>
      </defs>
      <polygon points="26,14 56,14 48,23 18,23" fill="var(--charcoal)"/>
      <polygon points="36,21 272,21 266,30 28,30" fill="var(--red)"/>
      <rect x="0" y="73" width="350" height="200" fill="var(--red)"/>
      <rect role="img" aria-label="Photo of two business people shaking hands before a city skyline" x="22" y="73" width="316" height="200" fill="url(#meeting)"/>
      <polygon points="28,467 318,467 312,475 20,475" fill="var(--charcoal)"/>
      <polygon points="280,467 330,467 324,475 274,475" fill="var(--red)"/>
    </svg>
    <div class="brand-header"><span class="brand-dot"></span><span>Studio<br>Lindqvara</span></div>
    <h2 class="image-title">2.&nbsp;&nbsp; IMAGE</h2>
    <span class="page-no">Page | 5</span>
  </div>
</section>

<!-- Back cover -->
<section class="page p6" aria-label="Back cover">
  <div class="sheet">
    <svg class="art" viewBox="0 0 350 493">
      <defs>
        <linearGradient id="cityBack" x1="0" y1="0" x2="1" y2="0">
          <stop offset="0" stop-color="var(--photo-a)"/>
          <stop offset="1" stop-color="var(--photo-b)"/>
        </linearGradient>
      </defs>
      <polygon points="0,0 350,0 350,262 0,215" fill="var(--charcoal)"/>
      <polygon role="img" aria-label="Photo of glass office towers" points="0,0 350,0 350,80 0,25" fill="url(#cityBack)"/>
      <polygon points="60,16 350,66 350,70 60,19" fill="var(--red)"/>
      <polygon points="0,215 120,210 220,250 350,262 350,322 290,290 250,360 210,340 0,285" fill="var(--red)"/>
      <polygon points="120,210 220,250 210,300 150,260" fill="var(--red-deep)"/>
      <polygon points="220,250 350,262 350,322 290,290 250,360 210,300" fill="var(--red-soft)"/>
    </svg>
    <div class="brand-back"><span class="brand-dot"></span><span>Studio Lindqvara</span></div>
  </div>
</section>

</body>
</html>
```